Business Card Design

Business sales of reconditioned / used batteries with mobile delivery and install services. Customers base majority are auto car sales lots and individuals.

Card need to convey quality product reliability and quick prompt professional service.

Card must reflect excellence in customer care and product being offered

Target Market(s)

Auto car lots new and used. Auto repair shops. Individuals.

Industry/Entity Type

Business

Contact Information for Business Card

Cells Q-Dash
Cars, Trucks, Boats, Motorcycles, lawn mowers, power tools
Delivery & install available most vehicles
Mon-Sat 9-6pm
Lyle Brockett 501-738-2054
*product warranty 6 month shelf life battery/1 year blems battery

```html
<!DOCTYPE html>
<html lang="en">
<head>
<meta charset="utf-8">
<title>Cells Q-Dash — Business Card</title>
<link href="https://fonts.googleapis.com/css2?family=Josefin+Sans:wght@400;700&display=swap" rel="stylesheet">
<style>
  :root {
    --page: #e4e2de;
    --card: #f1f0ec;
    --ink: #2c2c2c;
    --ink-soft: #4a4a4a;
    --brand-green: #79b843;
    --rule: #3a3a3a;
  }
  * { margin: 0; padding: 0; box-sizing: border-box; }
  html, body {
    width: 1200px; height: 918px; overflow: hidden;
    background: var(--page);
  }
  .canvas {
    position: relative; width: 1200px; height: 918px;
    display: flex; align-items: center; justify-content: center;
  }
  .card {
    position: relative; width: 1000px; height: 572px;
    background: var(--card);
    box-shadow: 0 6px 24px rgba(0,0,0,0.12);
    font-family: "Josefin Sans", sans-serif;
    color: var(--ink);
    text-transform: uppercase;
  }
  .brand {
    position: absolute; left: 110px; top: 130px;
    width: 490px;
    display: flex; align-items: center; gap: 14px;
  }
  .brand-mark {
    flex: none;
    width: 30px; height: 30px; background: var(--brand-green);
  }
  .brand-name {
    font-weight: 700; font-size: 48px; line-height: 1;
    color: var(--brand-green); letter-spacing: 1px;
    padding-top: 7px; white-space: nowrap;
  }
  .services {
    position: absolute; left: 110px; top: 228px;
    width: 500px;
    font-size: 23px; line-height: 1.2; color: var(--ink-soft);
    white-space: nowrap;
  }
  .services .gap { margin-top: 8px; }
  .warranty {
    position: absolute; left: 140px; top: 430px;
    width: 470px;
    font-size: 10.5px; letter-spacing: 0.4px; color: var(--ink-soft);
    white-space: nowrap;
  }
  .divider {
    position: absolute; left: 640px; top: 110px;
    width: 2px; height: 380px; background: var(--rule);
  }
  .contact {
    position: absolute; left: 680px; top: 135px;
    width: 290px;
    list-style: none; font-size: 24px; color: var(--ink-soft);
    white-space: nowrap;
  }
  .contact li { margin-bottom: 26px; }
  .contact svg { display: block; width: 34px; height: 34px; margin-bottom: 10px; fill: var(--ink); }
</style>
</head>
<body>
<main class="canvas">
  <section class="card" aria-label="Cells Q-Dash business card">
    <div class="brand">
      <span class="brand-mark" aria-hidden="true"></span>
      <h1 class="brand-name">Cells Q-Dash</h1>
    </div>

    <div class="services">
      <p>Cars, Trucks, Boats, Motorcycles,</p>
      <p>Lawn Mowers, Power Tools</p>
      <p class="gap">Delivery &amp; Install Available</p>
      <p>On Most Vehicles</p>
    </div>

    <p class="warranty">Product warranty 6 month shelf life battery/1 year blems battery</p>

    <div class="divider" aria-hidden="true"></div>

    <ul class="contact">
      <li class="contact-name">
        <svg viewBox="0 0 40 40" aria-hidden="true"><circle cx="20" cy="12" r="9"/><path d="M3 40c0-11 8-17 17-17s17 6 17 17z"/></svg>
        Lyle Brockett
      </li>
      <li class="contact-phone">
        <svg viewBox="0 0 40 40" aria-hidden="true"><path d="M4 14c0-5 7-8 16-8s16 3 16 8v3h-8v-4c-3-1-5-1-8-1s-5 0-8 1v4H4z"/><path d="M10 19h20l5 17H5z"/><circle cx="20" cy="27" r="4" fill="#f1f0ec"/></svg>
        501-738-2054
      </li>
      <li class="contact-hours">
        <svg viewBox="0 0 40 40" aria-hidden="true"><rect x="16" y="1" width="8" height="5"/><circle cx="20" cy="23" r="16"/><circle cx="20" cy="23" r="11" fill="#f1f0ec"/><rect x="19" y="14" width="2.5" height="10"/></svg>
        Mon-Sat 9-6PM
      </li>
    </ul>
  </section>
</main>
</body>
</html>
```